bluegum voyages

We provide boar charter for :Fishing/whale watching and diving in Sydney Harbour providing for 12 passengersI have yet to have web page made but want to make logo first then do web page later. So I want to be able to edit and add this site to card later

Contact Information for Business Card

Captain Len (Doc) Wigellphone no 0457710098email awigell4@gmail.comCompany name Marlow Outings Pty Ltd in association with far reef cruises

Font styles to use
Serif

Requirements
Nice to have
• perhaps a photo of boat and some stick diagrams of fishing.whales and diviving

```html
<!DOCTYPE html>
<html lang="en">
<head>
<meta charset="utf-8">
<title>Marlow Outings Pty Ltd – Business Card</title>
<link rel="stylesheet" href="https://fonts.googleapis.com/css2?family=Ubuntu:wght@400;700&family=Raleway:wght@300;400;700&display=swap">
<style>
  :root {
    --backdrop: #e9ecef;
    --card-white: #ffffff;
    --card-mist: #e6e8eb;
    --navy: #154579;
    --sky: #2a9fd8;
    --sea-deep: #2c5a86;
    --sea-sky: #8fc3ea;
    --text-light: #ffffff;
  }
  * { margin: 0; padding: 0; box-sizing: border-box; }
  html, body {
    width: 1200px; height: 1000px; overflow: hidden;
    background: var(--backdrop);
  }
  .canvas {
    position: relative; width: 1200px; height: 1000px;
    display: flex; flex-direction: column; align-items: center; justify-content: center; gap: 60px;
  }
  .card {
    width: 720px; height: 400px; border-radius: 26px; overflow: hidden;
    box-shadow: 0 10px 28px rgba(20, 40, 70, 0.18);
  }
  .card svg { display: block; }
  .brand-name { font-family: "Ubuntu", sans-serif; font-weight: 700; fill: var(--sky); }
  .web-address { font-family: "Raleway", sans-serif; font-weight: 400; fill: var(--text-light); letter-spacing: 1px; }
  .captain-name { font-family: "Ubuntu", sans-serif; font-weight: 700; fill: var(--text-light); }
  .service-lead { font-family: "Raleway", sans-serif; font-weight: 700; fill: var(--text-light); }
  .service-line { font-family: "Raleway", sans-serif; font-weight: 300; fill: var(--text-light); }
  .contact-line { font-family: "Raleway", sans-serif; font-weight: 300; fill: var(--text-light); }
</style>
</head>
<body>
<main class="canvas">

  <!-- Front: brand side -->
  <section class="card card-front" aria-label="Business card front">
    <svg width="720" height="400" viewBox="0 0 720 400">
      <defs>
        <linearGradient id="frontShade" x1="0" y1="0" x2="0" y2="1">
          <stop offset="0" stop-color="var(--card-white)"/>
          <stop offset="1" stop-color="var(--card-mist)"/>
        </linearGradient>
      </defs>
      <rect class="front-base" width="720" height="400" fill="url(#frontShade)"/>
      <path class="front-band" d="M0 400 L0 340 C 200 370, 480 330, 720 210 L720 400 Z" fill="var(--navy)"/>
      <path class="front-swoosh" d="M0 332 C 200 362, 480 322, 720 196" fill="none" stroke="var(--sky)" stroke-width="6"/>
      <g class="brand-lockup">
        <circle cx="190" cy="150" r="26" fill="var(--sky)"/>
        <text class="brand-name" x="230" y="162" font-size="32">Marlow Outings Pty Ltd</text>
      </g>
      <text class="web-address" x="360" y="360" font-size="22" text-anchor="middle" transform="rotate(-10 360 360)">www.yourwebhere.com</text>
    </svg>
  </section>

  <!-- Back: contact side -->
  <section class="card card-back" aria-label="Business card back">
    <svg width="720" height="400" viewBox="0 0 720 400">
      <defs>
        <linearGradient id="harbourTones" x1="0" y1="0" x2="0" y2="1">
          <stop offset="0" stop-color="var(--sea-sky)"/>
          <stop offset="0.5" stop-color="#dfe8ee"/>
          <stop offset="1" stop-color="var(--sea-deep)"/>
        </linearGradient>
      </defs>
      <rect class="back-base" width="720" height="400" fill="var(--navy)"/>
      <path class="photo-arc" d="M352 0 C 452 120 452 280 382 400" fill="none" stroke="var(--card-white)" stroke-width="7"/>
      <path class="boat-photo" role="img" aria-label="Photo of a white charter boat speeding across Sydney Harbour" d="M0 0 H340 C 440 120 440 280 370 400 H0 Z" fill="url(#harbourTones)"/>

      <text class="captain-name" x="462" y="92" font-size="36">Captain Len</text>
      <text class="service-lead" x="462" y="138" font-size="16">We provide boar charter for</text>
      <text class="service-line" x="462" y="164" font-size="18">Fishing</text>
      <text class="service-line" x="462" y="190" font-size="18">whale watching and</text>
      <text class="service-line" x="462" y="216" font-size="18">diving in Sydney Harbour</text>

      <g class="contact-phone">
        <circle cx="476" cy="286" r="13" fill="var(--card-white)"/>
        <rect x="471" y="277" width="10" height="18" rx="2" fill="var(--navy)"/>
        <rect x="473" y="280" width="6" height="7" fill="var(--card-white)"/>
        <text class="contact-line" x="498" y="293" font-size="20">0468231594</text>
      </g>
      <g class="contact-email">
        <circle cx="476" cy="326" r="13" fill="var(--card-white)"/>
        <rect x="468" y="320" width="16" height="11" fill="var(--navy)"/>
        <path d="M468 320 L476 327 L484 320" fill="none" stroke="var(--card-white)" stroke-width="1.5"/>
        <text class="contact-line" x="498" y="333" font-size="18">lpruntel7@tidewake.net</text>
      </g>
    </svg>
  </section>

</main>
</body>
</html>
```